VistaLume webpage - Design only no coding required

Please refer to "web content" uploaded 23rd Sep for content

We are a digital signage company based in Jakarta, Indonesia.

Our core business is placement of LCD Tv's in waiting rooms of various hospitals in Indonesia which plays educational videos regarding various health topics (prescription/ethical medicines), OTC drugs TVC and other FMCG and ads.

Our client portfolio consists of the worlds biggest and well known Pharmaceutical companies and also local pharmaceutical companies.

Other parts of our business are as follows:
- Patient symposiums
- Booths for product activation
- Queuing systems that we have developed in house that use an android tablet and connect to our TV's
- Branding. eg. Lift doors, banners (static signage)
- Hospital management software. Specially developed software that comes in a generic format and needs to be customized to suit each hospital. It manages everything for phone/web booking, queues, registration, patient records, doctors schedules, referrals, pharmacy and inventory and checkout/payments.

We are after a website redesign that is visually attractive and modern as we also deal with many advertising agencies.

Our logo is orange and black, however the black & white can be reversed if necessary.

Pages will need to be available in English & Bahasa Indonesia language formats.

I am happy to answer any questions asap, i can be contacted at info@vistalume.example.id

current site (www.vistalume.example.id)

Target Market(s)

Mainly our business is B2B dealing with advertising clients either directly or through ad agencies.

The other aspect of our target market is hospitals where we place our screens.

There is (but not largely) and consumer audience.

In summary:
We have the following target markets:
1. Advertisers/ad agencies
2. Hospitals that wish to use our business model to display content to their patients 3. We are in a developing country however most of our viewers and clients are from a high demographic profile

Industry/Entity Type

Pharmaceutical

Requirements
Must have
• We will require duplicates of the pages in English & Bahasa Indonesia

I would like the initial designs with a focus on being clean yet bold and emphasis on typography.

The following pages will be required (but not limited to) to qualify for the prize:

-Home

- About Us

- Services
(sub pages)
=Digital Signage
=Video Content Production
=Hospital Branding
=Event Management
=Seminar
=Queue System
=Hospital Management Software

-Why Choose Us?

- Contact Us

- Clients & Partners

- Gallery

Based on the "Nice to haves" site examples we do not necessarily require pictures of our LCD's/content on the main page(s) and would be happy to purchase required stock photos if needed/agreed.

We definitely want a modern feel and do not wish to overload with too much info on the main page.

(Please note the text in the attached file will most likely be changed once we have a design concept, probably less text)

Webpages we like:
http://www.brinklanternstudio.example/
http://quillharbor.example

Nice to have
• This is some of the international players which we want our site to look like:
www.pardelsign.example.au
http://www.morvexpanel.example.uk/
www.tallowgrid.example/

Should not have
• We prefer not to have old outdated fonts and a website that resembles anything like the current one, we are after a modern and professional feel.
These are some of our relative competitors of which we DO NOT want our website looking like but as a reference:
http://curabyte-global.example/index.html
http://zrk.example.id/

```html
<!DOCTYPE html>
<html lang="en">
<head>
<meta charset="utf-8">
<title>VistaLume — Digital Signage in Hospitals</title>
<link rel="stylesheet" href="https://fonts.googleapis.com/css2?family=PT+Sans:wght@400;700&family=Noto+Serif&display=swap">
<style>
:root{
  --orange:#f7941d;
  --black:#000;
  --ink:#222;
  --muted:#8a8a8a;
  --footer:#3a3a3a;
  --footer-deep:#2a2a2a;
  --footer-text:#cfcfcf;
  --white:#fff;
  --link-blue:#1f4fa8;
}
*{margin:0;padding:0;box-sizing:border-box}
html,body{width:1200px;height:2546px;overflow:hidden;background:var(--white)}
body{position:relative;font-family:"PT Sans",Arial,sans-serif;color:var(--ink)}

/* header */
.site-header{position:absolute;left:0;top:0;width:1200px;height:112px;background:var(--black)}
.brand{position:absolute;left:88px;top:32px;display:flex;align-items:center;gap:12px;color:var(--white);font-weight:700;font-size:36px}
.brand-mark{width:40px;height:40px;background:var(--orange)}
.social{position:absolute;left:950px;top:52px;display:flex;gap:8px}
.social span{width:26px;height:26px;border-radius:50%;display:block}

.main-nav{position:absolute;left:0;top:112px;width:1200px;height:53px;background:linear-gradient(#333,#232323);border-top:1px solid #444}
.main-nav a{position:absolute;top:14px;font-family:"Noto Serif",Georgia,serif;font-size:18px;color:#e8e8e8;text-decoration:none;white-space:nowrap}
.main-nav a.active{color:var(--orange)}

/* hero */
.hero{position:absolute;left:0;top:165px;width:1200px;height:535px;
  background:linear-gradient(180deg,#c9e0ee 0%,#eef4f2 35%,#dfe7c6 60%,#a8a94a 80%,#5f6a1f 100%)}
.hero h1{position:absolute;left:0;width:1200px;text-align:center;font-weight:400;color:#111;line-height:1;white-space:nowrap}
.hero .l1{top:112px;font-size:40px}
.hero .l2{top:160px;font-size:50px;font-weight:700}
.hero .l3{top:224px;font-size:38px;color:var(--orange)}
.hero-arrow{position:absolute;top:378px;width:58px;height:58px}
.notch{position:absolute;left:582px;top:682px;width:0;height:0;border-left:18px solid transparent;border-right:18px solid transparent;border-bottom:18px solid var(--white)}

/* about */
.about-title{position:absolute;top:752px;left:0;width:1200px;text-align:center;font-size:46px;color:var(--orange);font-weight:400}
.about-lead{position:absolute;top:815px;left:0;width:1200px;text-align:center;font-size:21px;color:#333}
.about-body{position:absolute;top:855px;left:200px;width:800px;text-align:center;font-size:13.5px;line-height:21px;color:var(--muted)}
.btn{position:absolute;top:947px;height:41px;line-height:41px;text-align:center;font-size:16px;color:var(--white);text-transform:uppercase}
.btn-dark{left:446px;width:145px;background:var(--black)}
.btn-orange{left:608px;width:144px;background:var(--orange)}

/* why choose */
.why{position:absolute;left:0;top:1049px;width:1200px;height:581px;
  background:radial-gradient(ellipse at 30% 55%,#8a929a 0%,#5c636a 45%,#3f4448 100%);color:var(--white)}
.why h2{position:absolute;top:34px;left:0;width:1200px;text-align:center;font-size:44px;font-weight:400}
.why .rule{position:absolute;left:114px;top:122px;width:991px;height:3px;background:rgba(255,255,255,.45)}
.why p{position:absolute;left:150px;width:900px;text-align:center;font-size:13.5px;line-height:19px}
.why h3{position:absolute;top:363px;left:0;width:1200px;text-align:center;font-size:26px;font-weight:400}
.why .spec{position:absolute;top:405px;left:0;width:1200px;text-align:center;font-size:13.5px}
.btn-outline{position:absolute;left:407px;top:463px;width:421px;height:63px;border:2px solid #ddd;text-align:center;line-height:59px;font-size:21px}

/* services */
.services{position:absolute;left:0;top:1630px;width:1200px;height:463px;
  background:linear-gradient(180deg,#1e1e1e 0%,#4a3a2c 35%,#8b6a49 65%,#b08d68 100%);color:var(--white)}
.services h2{position:absolute;top:50px;left:0;width:1200px;text-align:center;font-size:46px;font-weight:400}
.svc{position:absolute;top:145px;width:112px;text-align:center}
.svc .ring{width:88px;height:88px;margin:0 auto;border-radius:50%;background:var(--white);border:4px solid #ddd;display:flex;align-items:center;justify-content:center}
.svc .label{margin-top:8px;font-size:18px;line-height:21px;text-shadow:0 1px 2px #000}
.tip{position:absolute;left:98px;top:300px;width:314px;height:146px;background:rgba(30,26,22,.88);border-radius:4px;padding:12px 16px;font-size:12.5px;line-height:17px}
.tip .more{position:absolute;right:20px;bottom:10px;color:#ffd23f}

/* partners */
.partners{position:absolute;left:0;top:2093px;width:1200px;height:169px;background:linear-gradient(#fafafa,#e2e2e2)}
.partners .arrow{position:absolute;top:50px;font-size:30px;color:var(--link-blue)}
.partner{position:absolute;top:62px;font-size:20px;font-weight:700;color:#666;transform:translateX(-50%);white-space:nowrap}

/* footer */
.site-footer{position:absolute;left:0;top:2262px;width:1200px;height:209px;background:var(--footer);color:var(--footer-text);font-family:Arial,sans-serif}
.fcol{position:absolute;top:20px}
.fcol h4{font-size:11.5px;font-weight:400;letter-spacing:.5px;margin-bottom:14px;text-transform:uppercase}
.fcol li{list-style:none;font-size:12px;line-height:18.4px}
.contact-row{position:absolute;left:784px;display:flex;gap:14px;font-size:12px;line-height:19px}
.contact-row svg{flex:none;margin-top:2px}
.bottom-bar{position:absolute;left:0;top:2471px;width:1200px;height:75px;background:var(--footer-deep)}
.bottom-bar p{position:absolute;left:826px;top:24px;font-size:11px;color:#bbb;font-family:Arial,sans-serif}
</style>
</head>
<body>

<header class="site-header">
  <div class="brand"><span class="brand-mark"></span>VistaLume</div>
  <div class="social" aria-label="Social links">
    <span style="background:#3b5998"></span>
    <span style="background:#2aa3e0"></span>
    <span style="background:#f28c1b"></span>
    <span style="background:#d9262b"></span>
  </div>
</header>

<nav class="main-nav">
  <a class="active" style="left:119px">Home</a>
  <a style="left:224px">About Us</a>
  <a style="left:353px">Services ▾</a>
  <a style="left:477px">Why Choose Us?</a>
  <a style="left:671px">Contact Us</a>
  <a style="left:814px">Clients &amp; Partners</a>
  <a style="left:1019px">Gallery</a>
</nav>

<section class="hero" role="img" aria-label="Children running across a sunlit grassy field under a bright sky">
  <h1 class="l1">WE ARE THE EASIEST ACCESS TO</h1>
  <h1 class="l2">CONDUCT PROMOTIONAL ACTIVITIES</h1>
  <h1 class="l3">IN HOSPITALS</h1>
</section>
<svg class="hero-arrow" style="left:54px" viewBox="0 0 58 58"><circle cx="29" cy="29" r="29" fill="#1a1a1a"/><path d="M33 19 L23 29 L33 39" stroke="#fff" stroke-width="4" fill="none"/></svg>
<svg class="hero-arrow" style="left:1089px" viewBox="0 0 58 58"><circle cx="29" cy="29" r="29" fill="#1a1a1a"/><path d="M25 19 L35 29 L25 39" stroke="#fff" stroke-width="4" fill="none"/></svg>
<div class="notch"></div>

<section class="about">
  <h2 class="about-title">Little About VistaLume</h2>
  <p class="about-lead">VistaLume facilitates marketing opportunities especially in the medical space direct to patients/customers</p>
  <p class="about-body">VistaLume is a company focused to assist with promotional activities and targets a different way. We are a company with access to a specific location is a hospital grade A and B are present to help spread awareness of products to target very specific as well as improved quality and a healthy lifestyle to the community through the promotion of educational content</p>
  <a class="btn btn-dark">Learn More</a>
  <a class="btn btn-orange">Get in Touch</a>
</section>

<section class="why" role="img" aria-label="Blurred photo of medical staff in a hospital room">
  <h2>Why Choose Us?</h2>
  <div class="rule"></div>
  <p style="top:153px">VistaLume is an advertising digital system, which uses a network of LCD television displays connected via internet.</p>
  <p style="top:193px">VistaLume provides relevant educational and promotional content to assist in providing better patient care, Information &amp; education, whilst stimulating interest in related products &amp; services.</p>
  <p style="top:253px">VistaLume places its screens in the waiting rooms of KOL, clinics and Hospitals within Jakarta, allowing advertisers to target specific segments.</p>
  <p style="top:294px">VistaLume is run by a professional team dedicated to providing exceptional service and a premium product.</p>
  <h3>Specialties</h3>
  <div class="spec">Digital Signage - Specialist for Pharmaceuticals, Digital Signage at Hospital, Digital Signage for Healthcare, Media Iklan Digital</div>
  <div class="btn-outline">Click here for More information</div>
</section>

<section class="services" role="img" aria-label="Hand touching a tablet on a wooden table">
  <h2>Services Provide</h2>
  <div class="svc" style="left:182px"><div class="ring"><svg width="40" height="40" viewBox="0 0 40 40"><rect x="4" y="6" width="32" height="22" fill="none" stroke="#444" stroke-width="3"/><rect x="16" y="30" width="8" height="4" fill="#444"/></svg></div><div class="label">Digital Signage</div></div>
  <div class="svc" style="left:311px"><div class="ring"><svg width="40" height="40" viewBox="0 0 40 40"><rect x="5" y="13" width="22" height="16" fill="#333"/><path d="M27 17 L36 12 V30 L27 25Z" fill="#333"/><circle cx="11" cy="9" r="4" fill="#333"/><circle cx="21" cy="9" r="4" fill="#333"/></svg></div><div class="label">Video Content Production</div></div>
  <div class="svc" style="left:443px"><div class="ring"><svg width="40" height="40" viewBox="0 0 40 40"><path d="M6 18 L20 6 L34 18 V34 H6Z" fill="#444"/><path d="M18 15h4v5h5v4h-5v5h-4v-5h-5v-4h5z" fill="#fff"/></svg></div><div class="label">Hospital Branding</div></div>
  <div class="svc" style="left:575px"><div class="ring"><svg width="40" height="40" viewBox="0 0 40 40"><rect x="6" y="8" width="28" height="26" rx="3" fill="#444"/><circle cx="15" cy="18" r="4" fill="#fff"/><circle cx="25" cy="18" r="4" fill="#fff"/><rect x="10" y="24" width="20" height="6" rx="3" fill="#fff"/></svg></div><div class="label">Event Management</div></div>
  <div class="svc" style="left:708px"><div class="ring"><svg width="40" height="40" viewBox="0 0 40 40"><rect x="16" y="6" width="20" height="14" fill="none" stroke="#444" stroke-width="2.5"/><circle cx="9" cy="12" r="4" fill="#444"/><path d="M5 34 V20 H13 V34Z" fill="#444"/><line x1="13" y1="20" x2="20" y2="15" stroke="#444" stroke-width="2"/></svg></div><div class="label">Seminar</div></div>
  <div class="svc" style="left:832px"><div class="ring"><svg width="44" height="40" viewBox="0 0 44 40"><g fill="#555"><circle cx="8" cy="10" r="3"/><rect x="5" y="14" width="6" height="18"/><circle cx="18" cy="10" r="3"/><rect x="15" y="14" width="6" height="18"/><circle cx="28" cy="10" r="3"/><rect x="25" y="14" width="6" height="18"/></g><circle cx="38" cy="10" r="3" fill="#d22"/><rect x="35" y="14" width="6" height="18" fill="#d22"/></svg></div><div class="label">Queue System</div></div>
  <div class="svc" style="left:956px"><div class="ring"><svg width="40" height="40" viewBox="0 0 40 40"><rect x="4" y="7" width="32" height="22" rx="2" fill="#444"/><path d="M8 19h6l3-6 4 11 3-5h8" stroke="#7fd36b" stroke-width="2" fill="none"/><rect x="15" y="30" width="10" height="4" fill="#444"/></svg></div><div class="label">Hospital Management Software</div></div>
  <div class="tip">Lcd tv media are placed in a hospital waiting room poly class a and b as a medium conveys the message better promotional messages (Ads) to promote the general products that have a segmented and targeted educational messages to promote ethical products (health products that can not be sold freely)<span class="more">More &gt;&gt;</span></div>
</section>

<section class="partners" aria-label="Clients and partners">
  <span class="arrow" style="left:110px">‹</span>
  <span class="partner" style="left:246px">Pellworth Media</span>
  <span class="partner" style="left:458px">Cardale Media</span>
  <span class="partner" style="left:664px">VistaLume</span>
  <span class="partner" style="left:830px">Halden Media</span>
  <span class="partner" style="left:980px">VistaLume</span>
  <span class="arrow" style="left:1056px">›</span>
</section>

<footer class="site-footer">
  <div class="fcol" style="left:158px"><h4>Sitemap</h4><ul><li>Home</li><li>About Us</li><li>Why Choose Us?</li><li>Contact Us</li><li>Clients &amp; Partners</li><li>Gallery</li></ul></div>
  <div class="fcol" style="left:392px"><h4>Serivces</h4><ul><li>Digital Signage</li><li>Video Content Production</li><li>Hospital Branding</li><li>Event Management</li><li>Seminar</li><li>Queue System</li><li>Hospital Management Software</li></ul></div>
  <div class="fcol" style="left:788px"><h4>Contact Us</h4></div>
  <div class="contact-row" style="top:50px"><svg width="16" height="20" viewBox="0 0 16 20"><path d="M8 0a7 7 0 0 1 7 7c0 5-7 13-7 13S1 12 1 7a7 7 0 0 1 7-7z" fill="#bbb"/><circle cx="8" cy="7" r="2.5" fill="#3a3a3a"/></svg><span>Graha Lentera Level 4, Suite 410, Kemang,<br>South Jakarta,<br>Jakarta 12730 Indonesia</span></div>
  <div class="contact-row" style="top:124px"><svg width="16" height="16" viewBox="0 0 16 16"><path d="M3 1l3 3-2 2c1 2 3 4 5 5l2-2 3 3-2 3C7 15 1 9 1 3z" fill="#bbb"/></svg><span>021 555 0147</span></div>
  <div class="contact-row" style="top:155px"><svg width="16" height="14" viewBox="0 0 16 14"><rect x="0" y="1" width="16" height="12" fill="#bbb"/><path d="M0 1l8 6 8-6" stroke="#3a3a3a" stroke-width="1.5" fill="none"/></svg><span>info@vistalume.example.id</span></div>
</footer>
<div class="bottom-bar"><p>© 2013 vistalume.example.id, All Rights Reserved</p></div>

</body>
</html>
```